Brindel's Coating & Renewal Letterhead Design We want to revamp out old traditional letterhead with the new logo designs that are attached. We are working on getting all our company items from vehicles, business, cards, t-shirts, letterhead to match. This should include company colors, fonts, and flow of items that we have attached below.

Industry/Entity Type

Construction Company

Font styles to use
Sans Serif
Other font styles liked:
• Bold with outline

Colors
ec1f27
ffffff

Requirements
Must have
• Company Name: Brindel's Coating & Renewal
• Address: 4217 SW 83rd Ter Marlow Cove fl 33418
• Office Number: (954) 555-0194
• Email: Brindelrenewal@quorvane.com
• License Number: CGC8064392
Nice to have
• Company Colors: red, white, black, and grey

```html
<!DOCTYPE html>
<html lang="en">
<head>
<meta charset="utf-8">
<title>Brindel's Coating &amp; Renewal — Letterhead</title>
<link rel="stylesheet" href="https://fonts.googleapis.com/css2?family=Open+Sans:wght@400;600;800&display=swap">
<style>
  :root {
    --brand-red: #ec4a23;
    --ink: #3a3a3a;
    --muted: #4a4a4a;
    --rule: #b9b9bb;
    --swoosh-grey: #bdbec0;
    --paper: #ffffff;
  }
  * { margin: 0; padding: 0; box-sizing: border-box; }
  html, body { width: 1040px; height: 1200px; overflow: hidden; background: var(--paper); }
  body { font-family: "Open Sans", Arial, sans-serif; color: var(--ink); }

  .letterhead { position: relative; width: 1040px; height: 1200px; background: var(--paper); }

  .brand { position: absolute; left: 98px; top: 40px; display: flex; align-items: center; gap: 14px; }
  .brand-mark { width: 22px; height: 22px; background: var(--brand-red); }
  .brand-name { font-weight: 800; font-size: 30px; line-height: 1.05; color: var(--brand-red); text-transform: uppercase; letter-spacing: 0.5px; }

  .contact { position: absolute; left: 681px; top: 32px; padding-left: 14px; border-left: 1.5px solid var(--rule); font-size: 16px; line-height: 20px; color: var(--muted); }
  .contact-row { display: flex; align-items: center; gap: 6px; }
  .contact-row svg { width: 13px; height: 13px; fill: var(--brand-red); flex: none; }

  .letter { position: absolute; left: 98px; top: 216px; width: 846px; font-size: 15.5px; }
  .issue-date { margin-bottom: 17px; }
  .recipient { line-height: 19px; margin-bottom: 52px; }
  .salutation { margin-bottom: 28px; }
  .letter-body p { line-height: 27.2px; text-align: justify; margin-bottom: 27px; hyphens: auto; }
  .closing { margin-top: 50px; }
  .signature { display: block; width: 240px; height: 26px; margin: 12px 0 12px; background: #e9e9ea; }
  .signer-name { font-size: 20px; font-weight: 600; color: var(--ink); }
  .signer-title { margin-top: 4px; }

  .footer { position: absolute; left: 0; top: 1040px; width: 1040px; height: 160px; }
  .footer svg { position: absolute; inset: 0; }
  .footer-text { position: absolute; color: #fff; font-weight: 600; font-size: 18px; line-height: 23px; }
  .license { left: 98px; top: 108px; }
  .company-address { right: 96px; top: 82px; text-align: right; }
</style>
</head>
<body>
<main class="letterhead">
  <header>
    <div class="brand">
      <span class="brand-mark"></span>
      <div class="brand-name">Brindel's<br>Coating &amp; Renewal</div>
    </div>
    <div class="contact">
      <div class="contact-row">
        <svg viewBox="0 0 16 16" aria-hidden="true"><path d="M3 1h3l1.5 4-2 1.3a9 9 0 0 0 4.2 4.2L11 8.5l4 1.5v3a2 2 0 0 1-2 2A13 13 0 0 1 1 3a2 2 0 0 1 2-2z"/></svg>
        <span>(954) 555-0194</span>
      </div>
      <div class="contact-row">
        <svg viewBox="0 0 16 16" aria-hidden="true"><path d="M1 3h14v10H1z M2 4l6 5 6-5" stroke="#fff" stroke-width="1.4"/></svg>
        <span>Brindelrenewal@quorvane.com</span>
      </div>
    </div>
  </header>

  <section class="letter">
    <p class="issue-date">Issuing Date: May 5, 2018</p>
    <p class="recipient">Name Of Employee Mr. XYZABC<br>Address of Employee<br>Address Line 2 etc..</p>
    <p class="salutation">Dear Mr.XYZABC</p>
    <div class="letter-body">
      <p>Lorem Ipsum has been the industry's standard dummy text ever since the 1500s, when an unknown printer took a galley of type and scrambled it to make a type specimen book. It has survived not only five centuries, but also the leap into electronic typesetting, remaining essentially unchanged. It was popularised in the 1960s with the release of Dravtone sheets containing Lorem Ipsum passages, and more recently with desktop publishing software like Quillset Composer including versions of Lorem Ipsum.</p>
      <p>Lorem Ipsum is simply dummy text of the printing and typesetting industry. Lorem Ipsum has been the industry's standard dummy text ever since the 1500s, when an unknown printer took a galley of type and scrambled it to make a type specimen book.</p>
      <p>It has survived not only five centuries, but also the leap into electronic typesetting, remaining essentially unchanged. It was popularised in the 1960s with the release of Dravtone sheets containing Lorem IpsumIpsum passages.</p>
    </div>
    <div class="closing">
      <p>Yours Sincerely</p>
      <span class="signature" role="img" aria-label="Handwritten signature of Corwin Aldous"></span>
      <p class="signer-name">Corwin Aldous</p>
      <p class="signer-title">Managing Director</p>
    </div>
  </section>

  <footer class="footer">
    <svg viewBox="0 0 1040 160" preserveAspectRatio="none" aria-hidden="true">
      <path fill="var(--swoosh-grey)" d="M0,2 C120,62 220,92 330,90 C450,86 540,60 626,40 C520,58 420,76 330,78 C200,80 90,58 0,30 Z"/>
      <path fill="var(--brand-red)" d="M0,44 C120,80 220,94 310,94 C500,92 640,30 800,20 C900,14 980,12 1040,16 L1040,160 L0,160 Z"/>
    </svg>
    <p class="footer-text license">License Number: CGC8064392</p>
    <p class="footer-text company-address">BRINDEL'S COATING &amp; RENEWAL<br>4217 SW 83rd Ter Marlow Cove fl 33418</p>
  </footer>
</main>
</body>
</html>
```